Looking for a PowerPoint design for a Pharmaceutical Company

We need a PowerPoint template design to be used company-wide. We are a pharmaceutical company with 63 years of history and want to use a new template design to work more efficiently and effectively. Below are some of the things we are looking for in the new template design.

- Simple, modern, and professional

- Practical for every day use (easy to read, easy to create)

- Slides will be mainly projected or viewed on screens, but should also work fine when printed. (e.g. We do not want to use up our inks / toners printing several pages..)

- It would be great if you could provide us a list of colors that can be effectively used in the slides. (e.g. for highlighting fonts / multiple graph colors / etc.)

- Just as an FYI, our current logo image is (dark) blue. I am not uploading the logo image here because we do not want you to be limited by the current logo image. Depending on the design, we may / may not put our logo image on the slides.

Please feel free to reach out to me if you have any questions. I look forward to seeing your design. Thank you!

Target Market(s)

Pharmaceutical industry. (To be used internally and externally)

Industry/Entity Type

Pharmaceutical

Font styles to use
Sans Serif

Requirements
Must have
• Title slide, Subtitle slide, graphs, charts, tables, bullet points, and any other slide style components normally included.
Nice to have
• - As we are in the pharma industry, we want the slides to give credibility. But we do not want it look "old", "boring", or "typical". Feel free to use unique / fresh colors.
Should not have
• - TOO many colors
• - Please do not use the images on our website, which contain faces. (Any image with faces in it...) They are stock images we bought for the website, and we do not want the images on our slides. (e.g. image of running woman on the main page, image of a surgeon, image of kids playing soccer, etc.)
• - We are not looking for a design that is a modified version of our website design. We are looking for something new.

```html
<!DOCTYPE html>
<html lang="en">
<head>
<meta charset="utf-8">
<title>Corvia Health – Presentation Template Overview</title>
<link href="https://fonts.googleapis.com/css2?family=Roboto:wght@300;400;500;700&display=swap" rel="stylesheet">
<style>
:root{
  --blue:#1f48a6;
  --blue-mid:#3b63bd;
  --blue-soft:#7d9fd8;
  --blue-pale:#b9cbeb;
  --navy:#15357f;
  --gray:#b5b7bb;
  --gray-text:#7b7e84;
  --ink:#4a4d52;
  --canvas:#dfe0e2;
  --white:#ffffff;
}
*{margin:0;padding:0;box-sizing:border-box}
html,body{width:1200px;height:892px;overflow:hidden;background:var(--canvas);font-family:"Roboto",Arial,sans-serif;color:var(--ink)}
.deck{position:absolute;left:178px;top:28px;display:grid;grid-template-columns:repeat(3,289px);grid-auto-rows:163px;column-gap:6px;row-gap:6px}
.slide{position:relative;width:289px;height:163px;background:var(--white);overflow:hidden}
.abs{position:absolute}
.head{position:absolute;left:17px;top:12px;border-left:.7px solid var(--blue);padding-left:4px}
.head h2{font-weight:300;font-size:7.2px;color:var(--blue);letter-spacing:.1px;line-height:1}
.head p{font-size:3.4px;color:var(--gray-text);margin-top:1.5px;letter-spacing:.1px}
.brand{position:absolute;right:9px;top:10px;font-weight:400;font-size:5.6px;color:var(--navy);letter-spacing:.1px;white-space:nowrap}
.foot{position:absolute;left:0;right:0;bottom:0;height:3.6px;background:var(--blue);display:flex;justify-content:space-between;align-items:center;padding:0 8px;font-size:1.9px;color:var(--white)}
.fine{font-size:3px;line-height:1.45;color:var(--gray-text);text-align:justify}
.fine.c{text-align:center}
.white{color:var(--white)}
.photo{position:absolute}
</style>
</head>
<body>
<main class="deck">

  <section class="slide cover">
    <div class="brand" style="top:9px;font-size:8.2px">Corvia Health</div>
    <div class="abs" style="left:29px;top:40px;border-left:.8px solid var(--blue);padding-left:5px">
      <div style="font-size:5.6px;font-weight:300;color:var(--gray-text)">CORPORATE&nbsp;&nbsp;OVERVIEW</div>
      <div style="font-size:8px;font-weight:300;color:var(--blue);margin-top:1px">2016</div>
    </div>
    <div class="photo" role="img" aria-label="Runner on a grassy hillside at sunrise" style="left:0;top:65px;width:289px;height:72px;background:linear-gradient(180deg,#d8e3ea 0%,#c9d8d6 40%,#8fae5a 62%,#5e8a2e 100%)"></div>
    <div class="abs" style="left:20px;top:148px;font-size:2px;color:var(--gray-text)">© 2016 All rights reserved. Contents confidential and proprietary, not for distribution without written consent of the company.</div>
  </section>

  <section class="slide toc" style="background:var(--blue-mid)">
    <div class="photo" role="img" aria-label="Gloved hands holding a syringe, blue tinted" style="inset:0;background:radial-gradient(circle at 30% 50%,#5d80c8 0%,#3a62b8 45%,#2a53ad 100%)"></div>
    <div class="abs white" style="left:37px;top:42px">
      <div style="font-size:3.4px;font-weight:300">TABLE OF</div>
      <div style="font-size:9.5px;font-weight:300;margin-top:1px">CONTENTS</div>
      <div style="width:17px;height:.8px;background:var(--white);margin-top:3px"></div>
    </div>
    <div class="abs" style="left:141px;top:52px;width:123px">
      <div style="display:flex;flex-direction:column;gap:4.6px">
        <div style="display:flex;align-items:center;gap:2px"><span style="width:8px;height:8px;border-radius:50%;border:.6px solid #e8eef8;background:#8aa6da;color:#fff;font-size:3.6px;display:flex;align-items:center;justify-content:center">1</span><span style="flex:1;height:7px;background:#e4e8ef;font-size:3.5px;color:var(--blue);padding-left:4px;line-height:7px">LOREM IPSUM DOLOR SIT MET</span></div>
        <div style="display:flex;align-items:center;gap:2px"><span style="width:8px;height:8px;border-radius:50%;border:.6px solid #e8eef8;background:#8aa6da;color:#fff;font-size:3.6px;display:flex;align-items:center;justify-content:center">2</span><span style="flex:1;height:7px;background:#e4e8ef;font-size:3.5px;color:var(--blue);padding-left:4px;line-height:7px">LOREM IPSUM DOLOR SIT MET</span></div>
        <div style="display:flex;align-items:center;gap:2px"><span style="width:8px;height:8px;border-radius:50%;border:.6px solid #e8eef8;background:#8aa6da;color:#fff;font-size:3.6px;display:flex;align-items:center;justify-content:center">3</span><span style="flex:1;height:7px;background:#e4e8ef;font-size:3.5px;color:var(--blue);padding-left:4px;line-height:7px">LOREM IPSUM DOLOR SIT MET</span></div>
        <div style="display:flex;align-items:center;gap:2px"><span style="width:8px;height:8px;border-radius:50%;border:.6px solid #e8eef8;background:#8aa6da;color:#fff;font-size:3.6px;display:flex;align-items:center;justify-content:center">4</span><span style="flex:1;height:7px;background:#e4e8ef;font-size:3.5px;color:var(--blue);padding-left:4px;line-height:7px">LOREM IPSUM DOLOR SIT MET</span></div>
        <div style="display:flex;align-items:center;gap:2px"><span style="width:8px;height:8px;border-radius:50%;border:.6px solid #e8eef8;background:#8aa6da;color:#fff;font-size:3.6px;display:flex;align-items:center;justify-content:center">5</span><span style="flex:1;height:7px;background:#e4e8ef;font-size:3.5px;color:var(--blue);padding-left:4px;line-height:7px">LOREM IPSUM DOLOR SIT MET</span></div>
        <div style="display:flex;align-items:center;gap:2px"><span style="width:8px;height:8px;border-radius:50%;border:.6px solid #e8eef8;background:#8aa6da;color:#fff;font-size:3.6px;display:flex;align-items:center;justify-content:center">6</span><span style="flex:1;height:7px;background:#e4e8ef;font-size:3.5px;color:var(--blue);padding-left:4px;line-height:7px">LOREM IPSUM DOLOR SIT MET</span></div>
      </div>
    </div>
  </section>

  <section class="slide about-mosaic">
    <div class="head"><h2>ABOUT US</h2><p>SUB TITLE GOES HERE</p></div>
    <div class="brand">Corvia Health</div>
    <div class="abs" style="left:11px;top:41px;width:267px;display:grid;grid-template-columns:repeat(6,1fr);grid-template-rows:31px 31px;gap:1px">
      <div role="img" aria-label="Parent and child" style="background:linear-gradient(135deg,#a07a5c,#d8b49a)"></div>
      <div style="background:var(--blue);padding:2px" class="fine c white"><b style="font-size:2.8px">LOREM IPSUM</b><br>Dolor sit amet, consectetur adipiscing elit sed do eiusmod tempor</div>
      <div role="img" aria-label="Pills on a table" style="background:linear-gradient(135deg,#6b4a36,#c9a88a)"></div>
      <div style="background:var(--blue);padding:2px" class="fine c white"><b style="font-size:2.8px">LOREM IPSUM</b><br>Dolor sit amet, consectetur adipiscing elit sed do eiusmod tempor</div>
      <div role="img" aria-label="Laboratory glassware" style="background:linear-gradient(135deg,#e6ecf2,#9fb1c4)"></div>
      <div style="background:var(--blue);padding:2px" class="fine c white"><b style="font-size:2.8px">LOREM IPSUM</b><br>Dolor sit amet, consectetur adipiscing elit sed do eiusmod tempor</div>
      <div style="background:var(--blue-soft);padding:2px" class="fine c white"><b style="font-size:2.8px">LOREM IPSUM</b><br>Dolor sit amet, consectetur adipiscing elit sed do eiusmod</div>
      <div role="img" aria-label="Globe" style="background:radial-gradient(circle,#3a8ad0,#0e3d82)"></div>
      <div style="background:var(--blue-soft);padding:2px" class="fine c white"><b style="font-size:2.8px">LOREM IPSUM</b><br>Dolor sit amet, consectetur adipiscing elit sed do eiusmod</div>
      <div role="img" aria-label="Hands holding capsules" style="background:linear-gradient(135deg,#caa488,#7b5a48)"></div>
      <div style="background:var(--blue-soft);padding:2px" class="fine c white"><b style="font-size:2.8px">LOREM IPSUM</b><br>Dolor sit amet, consectetur adipiscing elit sed do eiusmod</div>
      <div role="img" aria-label="Green capsules" style="background:linear-gradient(135deg,#e8efe6,#6f9a6e)"></div>
    </div>
    <div class="abs" style="left:11px;top:105px;width:267px;height:38px;background:var(--blue);padding:10px 24px 0">
      <p class="fine c white" style="font-style:italic;font-size:3.2px">“Lorem ipsum dolor sit amet, consectetur adipiscing elit, sed do eiusmod tempor incididunt ut labore et dolore magna aliqua. Ut enim ad minim veniam, quis nostrud exercitation ullamco laboris nisi ut aliquip ex ea commodo consequat.”</p>
    </div>
    <div class="foot"><span>© 2016 All rights reserved</span><span>02</span></div>
  </section>

  <section class="slide about-band">
    <div class="head"><h2>ABOUT US</h2><p>SUB TITLE GOES HERE</p></div>
    <div class="brand">Corvia Health</div>
    <div class="abs" style="left:0;top:48px;width:95px;height:53px;background:var(--blue-soft);padding:17px 6px 0 17px">
      <p class="white" style="font-size:3px;line-height:1.5">LOREM IPSUM DOLOR SIT MET CONSECTETUR ADIPISCING ELIT, SED DO EIUSMOD TEMPOR INCIDIDUNT UT LABORE ET DOLORE MAGNA</p>
    </div>
    <div class="photo" role="img" aria-label="Pipette over blue and pink liquid in lab dishes" style="left:95px;top:48px;width:194px;height:53px;background:linear-gradient(100deg,#eef2f7 0%,#cfe3f5 30%,#3ea0e0 50%,#9fd0f0 65%,#f3d8e8 85%,#e07ab8 100%)"></div>
    <p class="fine abs" style="left:93px;top:107px;width:184px">Lorem ipsum dolor sit amet, consectetur adipiscing elit, sed do eiusmod tempor incididunt ut labore et dolore magna aliqua. Ut enim ad minim veniam, quis nostrud exercitation ullamco laboris nisi ut aliquip ex ea commodo consequat. Duis aute irure dolor in reprehenderit in voluptate velit esse cillum dolore eu fugiat nulla pariatur.</p>
    <div class="foot"><span>© 2016 All rights reserved</span><span>02</span></div>
  </section>

  <section class="slide vision" style="background:var(--blue-soft)">
    <div class="photo" role="img" aria-label="Children playing on a beach at dusk, blue tinted" style="left:0;top:0;width:289px;height:89px;background:linear-gradient(180deg,#3e66b8 0%,#4a72c0 55%,#5a80c8 100%)"></div>
    <div class="abs white" style="left:17px;top:13px;font-size:6.6px;font-weight:300">VISION &amp; MISSION</div>
    <svg class="abs" style="left:59px;top:67px" width="34" height="34" viewBox="0 0 34 34">
      <circle cx="17" cy="17" r="15" fill="var(--blue-soft)" stroke="#fff" stroke-width="1.2"/>
      <circle cx="13" cy="18" r="3.2" fill="none" stroke="#fff" stroke-width="1.4"/>
      <circle cx="21" cy="18" r="3.2" fill="none" stroke="#fff" stroke-width="1.4"/>
      <rect x="14.5" y="15.5" width="5" height="2" fill="#fff"/>
    </svg>
    <svg class="abs" style="left:180px;top:67px" width="34" height="34" viewBox="0 0 34 34">
      <circle cx="17" cy="17" r="15" fill="var(--blue-soft)" stroke="#fff" stroke-width="1.2"/>
      <path d="M10 21 A7 7 0 1 1 24 21" fill="none" stroke="#fff" stroke-width="1.4"/>
      <line x1="17" y1="20" x2="21" y2="14" stroke="#fff" stroke-width="1.4" stroke-linecap="round"/>
      <circle cx="17" cy="20" r="1.3" fill="#fff"/>
    </svg>
    <p class="fine c white abs" style="left:32px;top:106px;width:90px;font-size:4.3px;font-weight:300;line-height:1.3">To provide state of the art logistical and supply chain solutions to the defined needs of our customers using the best people, processes and systems in creating efficient and effective results.</p>
    <p class="fine c white abs" style="left:152px;top:106px;width:90px;font-size:4.3px;font-weight:300;line-height:1.3">To provide state of the art logistical and supply chain solutions to the defined needs of our customers using the best people, processes and systems in creating efficient and effective results.</p>
  </section>

  <section class="slide about-columns">
    <div class="head"><h2>ABOUT US</h2><p>SUB TITLE GOES HERE</p></div>
    <div class="brand">Corvia Health</div>
    <div class="photo" role="img" aria-label="Rows of glass vials" style="left:18px;top:52px;width:42px;height:32px;background:linear-gradient(90deg,#5f7890,#c9d8e4,#6d8aa6,#dce6ee)"></div>
    <p class="fine c abs" style="left:17px;top:87px;width:44px;color:var(--blue)">Lorem ipsum dolor sit amet consectetur adipiscing elit sed do eiusmod</p>
    <p class="fine abs" style="left:80px;top:53px;width:96px">Lorem ipsum dolor sit amet, consectetur adipiscing elit, sed do eiusmod tempor incididunt ut labore et dolore magna aliqua. Ut enim ad minim veniam, quis nostrud exercitation ullamco laboris nisi ut aliquip ex ea commodo consequat. Duis aute irure dolor in reprehenderit in voluptate velit esse cillum dolore eu fugiat nulla pariatur.<br><br>Lorem ipsum dolor sit amet, consectetur adipiscing elit, sed do eiusmod tempor incididunt ut labore et dolore magna aliqua. Ut</p>
    <p class="fine abs" style="left:181px;top:53px;width:96px">Lorem ipsum dolor sit amet, consectetur adipiscing elit, sed do eiusmod tempor incididunt ut labore et dolore magna aliqua. Ut enim ad minim veniam, quis nostrud exercitation ullamco laboris nisi ut aliquip ex ea commodo consequat. Duis aute irure dolor in reprehenderit in voluptate velit esse cillum dolore eu fugiat nulla pariatur.<br><br>Lorem ipsum dolor sit amet, consectetur adipiscing elit, sed do eiusmod tempor incididunt ut labore et dolore magna aliqua. Ut</p>
    <div class="foot"><span>© 2016 All rights reserved</span><span>02</span></div>
  </section>

  <section class="slide services">
    <div class="head"><h2>OUR SERVICES</h2><p>SUB TITLE GOES HERE</p></div>
    <div class="brand">Corvia Health</div>
    <div class="abs" style="left:20px;top:44px;width:252px;display:grid;grid-template-columns:repeat(4,1fr);gap:2px">
      <div>
        <div style="height:37px;background:var(--blue);display:flex;flex-direction:column;align-items:center;justify-content:flex-end;padding-bottom:3px">
          <svg width="12" height="12" viewBox="0 0 12 12"><path d="M6 1 L11 6 L6 11 L4 9 L6 6 L3 4 Z" fill="#fff"/></svg>
          <span style="font-size:3.4px;color:#fff;text-align:center;margin-top:2px;line-height:1.2">MANAGEMENT<br>SOLUTIONS</span>
        </div>
        <div style="height:58px;background:var(--blue-soft);padding:6px 3px" class="fine c white">Dolor sit amet, consectetur adipiscing elit, sed do eiusmod tempor incididunt ut labore et dolore magna aliqua.</div>
      </div>
      <div>
        <div style="height:37px;background:var(--blue-soft);display:flex;flex-direction:column;align-items:center;justify-content:flex-end;padding-bottom:3px">
          <svg width="12" height="12" viewBox="0 0 12 12"><circle cx="6" cy="6" r="5" fill="none" stroke="#fff" stroke-width=".9"/><rect x="5.4" y="5" width="1.2" height="4" fill="#fff"/><circle cx="6" cy="3.6" r=".7" fill="#fff"/></svg>
          <span style="font-size:3.4px;color:#fff;text-align:center;margin-top:2px;line-height:1.2">INFORMATION<br>SOLUTIONS</span>
        </div>
        <div style="height:58px;background:var(--blue);padding:6px 3px" class="fine c white">Dolor sit amet, consectetur adipiscing elit, sed do eiusmod tempor incididunt ut labore et dolore magna aliqua.</div>
      </div>
      <div>
        <div style="height:37px;background:var(--blue);display:flex;flex-direction:column;align-items:center;justify-content:flex-end;padding-bottom:3px">
          <svg width="13" height="12" viewBox="0 0 13 12"><path d="M1 5 L4 3 L7 5 L10 3 L12 5 L9 9 L5 9 Z" fill="#fff"/></svg>
          <span style="font-size:3.4px;color:#fff;text-align:center;margin-top:2px;line-height:1.2">PROFESSIONAL<br>SERVICES</span>
        </div>
        <div style="height:58px;background:var(--blue-soft);padding:6px 3px" class="fine c white">Dolor sit amet, consectetur adipiscing elit, sed do eiusmod tempor incididunt ut labore et dolore magna aliqua.</div>
      </div>
      <div>
        <div style="height:37px;background:var(--blue-soft);display:flex;flex-direction:column;align-items:center;justify-content:flex-end;padding-bottom:3px">
          <svg width="12" height="12" viewBox="0 0 12 12"><g stroke="#fff" stroke-width=".7"><line x1="6" y1="6" x2="2" y2="2"/><line x1="6" y1="6" x2="10" y2="3"/><line x1="6" y1="6" x2="3" y2="10"/><line x1="6" y1="6" x2="10" y2="9"/></g><circle cx="6" cy="6" r="1.8" fill="#fff"/><circle cx="2" cy="2" r="1" fill="#fff"/><circle cx="10" cy="3" r="1" fill="#fff"/><circle cx="3" cy="10" r="1" fill="#fff"/><circle cx="10" cy="9" r="1" fill="#fff"/></svg>
          <span style="font-size:3.4px;color:#fff;text-align:center;margin-top:2px;line-height:1.2">ORGANIZATIONAL<br>TRANSFORMATION</span>
        </div>
        <div style="height:58px;background:var(--blue);padding:6px 3px" class="fine c white">Dolor sit amet, consectetur adipiscing elit, sed do eiusmod tempor incididunt ut labore et dolore magna aliqua.</div>
      </div>
    </div>
    <div class="foot"><span>© 2016 All rights reserved</span><span>02</span></div>
  </section>

  <section class="slide data-table">
    <div class="head"><h2>OUR TABLE</h2><p>SUB TITLE GOES HERE</p></div>
    <div class="brand">Corvia Health</div>
    <div class="abs" style="left:61px;top:52px;width:166px;border:.5px solid #c9ccd2;padding:2px">
      <table style="width:100%;border-collapse:collapse;font-size:2.9px;color:#333">
        <thead><tr><th colspan="5" style="background:var(--blue);color:#fff;text-align:left;padding:1.2px 3px;font-size:3.8px;font-weight:500">Growth &amp; Income Investments</th></tr></thead>
        <tbody style="line-height:1.45">
          <tr style="border-bottom:.3px solid #ddd"><td>Oak Ridge</td><td>Sharon</td><td>IRA</td><td>$</td><td style="text-align:right">176,445.44</td></tr>
          <tr style="border-bottom:.3px solid #ddd"><td>North Asset Management</td><td>Trust</td><td>NQ</td><td>$</td><td style="text-align:right">211,514.52</td></tr>
          <tr style="border-bottom:.3px solid #ddd"><td>Summit Portfolio</td><td>Trust</td><td>NQ</td><td>$</td><td style="text-align:right">177,253.59</td></tr>
          <tr style="border-bottom:.3px solid #ddd"><td>Wellcare Trust Group</td><td>Ken</td><td>IRA</td><td>$</td><td style="text-align:right">269,704.35</td></tr>
          <tr style="border-bottom:.3px solid #ddd"><td>Silver</td><td>Ken</td><td>IRA</td><td>$</td><td style="text-align:right">37,766.03</td></tr>
          <tr style="border-bottom:.3px solid #ddd"><td>Lakeview</td><td>Ken</td><td>IRA</td><td>$</td><td style="text-align:right">47,654.15</td></tr>
          <tr style="border-bottom:.3px solid #ddd"><td>Lakeview</td><td>Sharon</td><td>IRA</td><td>$</td><td style="text-align:right">10,746.27</td></tr>
          <tr style="border-bottom:.3px solid #ddd"><td>Brightline</td><td>Ken</td><td>IRA</td><td>$</td><td style="text-align:right">77,123.47</td></tr>
          <tr style="border-bottom:.3px solid #ddd"><td>Cobalt Capital</td><td>Ken</td><td>IRA</td><td>$</td><td style="text-align:right">58,843.79</td></tr>
          <tr style="border-bottom:.3px solid #ddd"><td>Cobalt Capital</td><td>Sharon</td><td>IRA</td><td>$</td><td style="text-align:right">80,253.22</td></tr>
          <tr style="font-weight:700"><td colspan="3">Total Growth &amp; Income Investments</td><td>$</td><td style="text-align:right">1,147,560.59</td></tr>
        </tbody>
      </table>
    </div>
    <div class="foot"><span>© 2016 All rights reserved</span><span>02</span></div>
  </section>

  <section class="slide team">
    <div class="head"><h2>OUR TEAM</h2><p>SUB TITLE GOES HERE</p></div>
    <div class="brand">Corvia Health</div>
    <div class="abs" style="left:22px;top:43px;width:250px;display:grid;grid-template-columns:repeat(3,1fr);gap:12px;text-align:center">
      <div>
        <div role="img" aria-label="Portrait of Jonathan Doe" style="width:34px;height:34px;margin:0 auto;border-radius:50%;border:1.4px solid var(--blue);background:linear-gradient(180deg,#e9ecf0,#aab3bf)"></div>
        <div style="font-size:3.4px;color:var(--blue);margin-top:4px">JONATHAN DOE</div>
        <div style="font-size:2.6px;color:var(--gray-text)">President</div>
        <p class="fine c" style="margin-top:4px">dolor sit amet, consectetur adipiscing elit, sed do eiusmod tempor incididunt ut labore et dolore magna aliqua. Ut enim ad minim veniam, quis nostrud exercitation ullamco laboris nisi ut aliquip ex ea commodo.</p>
      </div>
      <div>
        <div role="img" aria-label="Portrait of Melanie Doe" style="width:34px;height:34px;margin:0 auto;border-radius:50%;border:1.4px solid var(--blue);background:linear-gradient(180deg,#eef0f3,#b9bec6)"></div>
        <div style="font-size:3.4px;color:var(--blue);margin-top:4px">MELANIE DOE</div>
        <div style="font-size:2.6px;color:var(--gray-text)">CEO / Founder</div>
        <p class="fine c" style="margin-top:4px">dolor sit amet, consectetur adipiscing elit, sed do eiusmod tempor incididunt ut labore et dolore magna aliqua. Ut enim ad minim veniam, quis nostrud exercitation ullamco laboris nisi ut aliquip ex ea commodo.</p>
      </div>
      <div>
        <div role="img" aria-label="Portrait of Natalie Doe" style="width:34px;height:34px;margin:0 auto;border-radius:50%;border:1.4px solid var(--blue);background:linear-gradient(180deg,#f1f2f4,#c2c6cc)"></div>
        <div style="font-size:3.4px;color:var(--blue);margin-top:4px">NATALIE DOE</div>
        <div style="font-size:2.6px;color:var(--gray-text)">Vice President</div>
        <p class="fine c" style="margin-top:4px">dolor sit amet, consectetur adipiscing elit, sed do eiusmod tempor incididunt ut labore et dolore magna aliqua. Ut enim ad minim veniam, quis nostrud exercitation ullamco laboris nisi ut aliquip ex ea commodo.</p>
      </div>
    </div>
    <div class="foot"><span>© 2016 All rights reserved</span><span>02</span></div>
  </section>

  <section class="slide bar-chart">
    <div class="head"><h2>OUR CHART</h2><p>SUB TITLE GOES HERE</p></div>
    <div class="brand">Corvia Health</div>
    <svg class="abs" style="left:0;top:0" width="289" height="163" viewBox="0 0 289 163">
      <g stroke="#999" stroke-width=".4"><line x1="38" y1="50" x2="38" y2="122"/><line x1="38" y1="122" x2="180" y2="122"/></g>
      <g font-size="2.2" fill="#999" text-anchor="end"><text x="36" y="123">0</text><text x="36" y="105">1</text><text x="36" y="87">2</text><text x="36" y="69">3</text><text x="36" y="52">4</text></g>
      <g>
        <rect x="45" y="58" width="7" height="64" fill="var(--blue)"/><rect x="52" y="96" width="7" height="26" fill="var(--gray)"/><rect x="59" y="101" width="7" height="21" fill="var(--blue-soft)"/>
        <rect x="79" y="85" width="7" height="37" fill="var(--blue)"/><rect x="86" y="62" width="7" height="60" fill="var(--gray)"/><rect x="93" y="101" width="7" height="21" fill="var(--blue-soft)"/>
        <rect x="113" y="76" width="7" height="46" fill="var(--blue)"/><rect x="120" y="103" width="7" height="19" fill="var(--gray)"/><rect x="127" y="93" width="7" height="29" fill="var(--blue-soft)"/>
        <rect x="147" y="74" width="7" height="48" fill="var(--blue)"/><rect x="154" y="95" width="7" height="27" fill="var(--gray)"/><rect x="161" y="74" width="7" height="48" fill="var(--blue-soft)"/>
      </g>
      <g font-size="2" fill="#fff" text-anchor="middle">
        <rect x="85" y="55" width="9" height="4" fill="var(--gray)"/><text x="89.5" y="58">13%</text>
        <rect x="112" y="69" width="9" height="4" fill="var(--blue)"/><text x="116.5" y="72">12%</text>
        <rect x="126" y="86" width="9" height="4" fill="var(--blue-soft)"/><text x="130.5" y="89">9%</text>
      </g>
      <g font-size="4.8" fill="#555" text-anchor="middle"><text x="56" y="131">2009</text><text x="90" y="131">2010</text><text x="124" y="131">2011</text><text x="158" y="131">2012</text></g>
      <g>
        <rect x="196" y="60" width="3" height="3" fill="var(--blue)"/><text x="202" y="62.6" font-size="2.8" fill="var(--blue)">LOREM IPSUM</text>
        <rect x="196" y="85" width="3" height="3" fill="var(--gray)"/><text x="202" y="87.6" font-size="2.8" fill="var(--blue)">LOREM IPSUM</text>
        <rect x="196" y="109" width="3" height="3" fill="var(--blue-soft)"/><text x="202" y="111.6" font-size="2.8" fill="var(--blue)">LOREM IPSUM</text>
      </g>
    </svg>
    <p class="fine abs" style="left:202px;top:64px;width:60px;font-size:2.5px">Lorem ipsum dolor sit amet, consectetur adipiscing elit, sed do eiusmod tempor incididunt.</p>
    <p class="fine abs" style="left:202px;top:89px;width:60px;font-size:2.5px">Lorem ipsum dolor sit amet, consectetur adipiscing elit, sed do eiusmod tempor incididunt.</p>
    <p class="fine abs" style="left:202px;top:113px;width:60px;font-size:2.5px">Lorem ipsum dolor sit amet, consectetur adipiscing elit, sed do eiusmod tempor incididunt.</p>
    <div class="foot"><span>© 2016 All rights reserved</span><span>02</span></div>
  </section>

  <section class="slide donut-chart">
    <div class="head"><h2>OUR CHART</h2><p>SUB TITLE GOES HERE</p></div>
    <div class="brand">Corvia Health</div>
    <svg class="abs" style="left:0;top:0" width="289" height="163" viewBox="0 0 289 163">
      <g fill="none" stroke-width="3.2">
        <circle cx="60" cy="68" r="16" stroke="#c3c7cf"/>
        <circle cx="60" cy="68" r="16" stroke="var(--navy)" stroke-dasharray="81.4 100.5" transform="rotate(-90 60 68)"/>
        <circle cx="144" cy="68" r="16" stroke="#c3c7cf"/>
        <circle cx="144" cy="68" r="16" stroke="var(--blue-soft)" stroke-dasharray="72.4 100.5" transform="rotate(-90 144 68)"/>
        <circle cx="228" cy="68" r="16" stroke="#c3c7cf"/>
        <circle cx="228" cy="68" r="16" stroke="var(--navy)" stroke-dasharray="63.3 100.5" transform="rotate(-90 228 68)"/>
      </g>
      <g font-size="7" font-weight="700" text-anchor="middle"><text x="60" y="70.5" fill="var(--navy)">81%</text><text x="144" y="70.5" fill="var(--blue-mid)">72%</text><text x="228" y="70.5" fill="var(--navy)">63%</text></g>
    </svg>
    <p class="fine c abs" style="left:30px;top:94px;width:60px">dolor sit amet, consectetur adipiscing elit, sed do eiusmod tempor incididunt ut labore et dolore magna aliqua. Ut enim ad minim veniam, quis nostrud exercitation ullamco laboris nisi ut aliquip ex ea commodo consequat.</p>
    <p class="fine c abs" style="left:114px;top:94px;width:60px">dolor sit amet, consectetur adipiscing elit, sed do eiusmod tempor incididunt ut labore et dolore magna aliqua. Ut enim ad minim veniam, quis nostrud exercitation ullamco laboris nisi ut aliquip ex ea commodo consequat.</p>
    <p class="fine c abs" style="left:198px;top:94px;width:60px">dolor sit amet, consectetur adipiscing elit, sed do eiusmod tempor incididunt ut labore et dolore magna aliqua. Ut enim ad minim veniam, quis nostrud exercitation ullamco laboris nisi ut aliquip ex ea commodo consequat.</p>
    <div class="foot"><span>© 2016 All rights reserved</span><span>02</span></div>
  </section>

  <section class="slide line-chart">
    <div class="head"><h2>OUR CHART</h2><p>SUB TITLE GOES HERE</p></div>
    <div class="brand">Corvia Health</div>
    <svg class="abs" style="left:0;top:0" width="289" height="163" viewBox="0 0 289 163">
      <g stroke="#d5d8dd" stroke-width=".35" stroke-dasharray="1 1">
        <line x1="32" y1="48" x2="160" y2="48"/><line x1="32" y1="63" x2="160" y2="63"/><line x1="32" y1="78" x2="160" y2="78"/><line x1="32" y1="93" x2="160" y2="93"/><line x1="32" y1="108" x2="160" y2="108"/>
      </g>
      <g stroke="#777" stroke-width=".4"><line x1="32" y1="45" x2="32" y2="124"/><line x1="32" y1="124" x2="162" y2="124"/></g>
      <polyline fill="none" stroke="var(--gray)" stroke-width=".9" points="34,88 50,84 64,91 78,112 92,98 106,95 120,103 134,88 148,75 158,94"/>
      <polyline fill="none" stroke="var(--blue-soft)" stroke-width=".9" points="34,90 50,81 64,83 78,80 92,84 106,71 120,82 134,66 148,78 158,86"/>
      <polyline fill="none" stroke="var(--navy)" stroke-width="1" points="34,86 50,73 64,99 78,89 92,89 106,55 120,94 134,80 148,71 158,80"/>
      <g fill="var(--navy)"><circle cx="50" cy="73" r="1"/><circle cx="64" cy="99" r="1"/><circle cx="106" cy="55" r="1"/><circle cx="148" cy="71" r="1"/></g>
      <g font-size="2" fill="#999" text-anchor="middle"><text x="44" y="129">100</text><text x="61" y="129">200</text><text x="78" y="129">300</text><text x="95" y="129">400</text><text x="112" y="129">500</text><text x="129" y="129">600</text><text x="146" y="129">700</text></g>
    </svg>
    <div class="abs" style="left:181px;top:58px;width:92px">
      <div style="font-size:7px;font-weight:300;color:var(--navy)">20%</div>
      <p class="fine" style="text-align:left;margin-bottom:4px">Lorem ipsum dolor sit amet, consectetur adipiscing elit, sed</p>
      <div style="font-size:7px;font-weight:300;color:var(--gray-text)">20%</div>
      <p class="fine" style="text-align:left;margin-bottom:4px">Lorem ipsum dolor sit amet, consectetur adipiscing elit, sed</p>
      <div style="font-size:7px;font-weight:300;color:var(--blue-soft)">20%</div>
      <p class="fine" style="text-align:left">Lorem ipsum dolor sit amet, consectetur adipiscing elit, sed</p>
    </div>
    <div class="foot"><span>© 2016 All rights reserved</span><span>02</span></div>
  </section>

  <section class="slide image-text">
    <div class="abs" style="left:0;top:0;width:124px;height:163px;background:var(--blue)"></div>
    <div class="abs white" style="left:17px;top:13px;font-size:6.6px;font-weight:300">IMAGE TEXT</div>
    <p class="fine white abs" style="left:17px;top:63px;width:94px;font-size:3.3px">Lorem ipsum dolor sit amet, consectetur adipiscing elit, sed do eiusmod tempor incididunt ut labore et dolore magna aliqua. Ut enim ad minim veniam, quis nostrud exercitation ullamco laboris nisi ut aliquip ex ea commodo consequat. Duis aute irure dolor in reprehenderit in voluptate velit esse cillum dolore eu fugiat nulla pariatur.</p>
    <div class="abs" style="left:4px;top:147px;background:#fff;padding:1px 3px;font-weight:400;font-size:4.6px;color:var(--navy)">Corvia Health</div>
    <div class="photo" role="img" aria-label="Medical professional in surgical scrubs" style="left:124px;top:0;width:165px;height:163px;background:linear-gradient(90deg,#eef3f8 0%,#d6e6f2 45%,#8fc0e2 70%,#dbe8f2 100%)"></div>
  </section>

  <section class="slide section-divider" style="background:var(--blue)">
    <div class="photo" role="img" aria-label="Hand with a syringe, deep blue tinted" style="inset:0;background:radial-gradient(circle at 55% 30%,#4a72c4 0%,#2b54ae 50%,#1f48a6 100%)"></div>
    <svg class="abs" style="left:127px;top:66px" width="35" height="35" viewBox="0 0 35 35">
      <circle cx="17.5" cy="17.5" r="16.5" fill="#fff"/>
      <circle cx="18.5" cy="9.5" r="2.6" fill="var(--blue)"/>
      <path d="M14 14 h6 l-3 12 h3 l-.6 2 h-7 l.6-2 h1.8 l2.4-10 h-3.6 Z" fill="var(--blue)"/>
    </svg>
    <div class="abs" style="left:107px;top:108px;width:75px;height:.6px;background:#fff"></div>
    <div class="abs white" style="left:0;width:289px;top:112px;text-align:center;font-size:6.8px;font-weight:300">SECTION TITLE</div>
  </section>

  <section class="slide closing">
    <div class="brand" style="top:10px;right:9px;font-size:9.5px">Corvia Health</div>
    <div class="abs" style="left:25px;top:39px;border-left:.8px solid var(--blue);padding-left:5px;line-height:1.05">
      <div style="font-size:6.6px;font-weight:300;color:var(--gray-text)">THANK YOU</div>
      <div style="font-size:8px;font-weight:300;color:var(--blue)">FOR YOUR TIME</div>
    </div>
    <div class="photo" role="img" aria-label="Company headquarters building facade" style="left:0;top:65px;width:289px;height:70px;background:linear-gradient(100deg,#c8ccd2 0%,#e6e9ee 30%,#8a96a6 55%,#d2d6dc 75%,#e8eaee 100%)"></div>
    <div class="abs" style="left:25px;top:144px;display:flex;gap:18px;font-size:3px;color:var(--gray-text);align-items:center">
      <span style="display:flex;align-items:center;gap:2px"><svg width="6" height="6" viewBox="0 0 10 10"><path d="M5 1 L9 5 H8 V9 H6 V6.5 H4 V9 H2 V5 H1 Z" fill="var(--blue)"/></svg>1200 Harbor Lane Ste 400</span>
      <span style="display:flex;align-items:center;gap:2px;margin-left:8px"><svg width="6" height="6" viewBox="0 0 10 10"><circle cx="5" cy="5" r="4.5" fill="var(--blue)"/><rect x="2.6" y="3.3" width="4.8" height="3.4" fill="none" stroke="#fff" stroke-width=".7"/></svg>hello@corviahealth.com</span>
      <span style="display:flex;align-items:center;gap:2px;margin-left:20px"><svg width="6" height="6" viewBox="0 0 10 10"><circle cx="5" cy="5" r="4.5" fill="var(--blue)"/><circle cx="5" cy="5" r="2.4" fill="none" stroke="#fff" stroke-width=".6"/><line x1="2.6" y1="5" x2="7.4" y2="5" stroke="#fff" stroke-width=".5"/></svg>www.corviahealth.com</span>
    </div>
    <div class="abs" style="left:0;right:0;bottom:0;height:2.5px;background:var(--blue)"></div>
  </section>

</main>
</body>
</html>
```